DELVOR Flyer

We would like the option of being able to fill in a text box so we would need an editable file to type in our information.
You can add wording to it yourself where you see fit
We would like better designs than the ones we are sending as well.
We would like the cedar vale logo add on the flyer. We want the exact logo but not the back ground. We would like the logo to show up multiple times if possible.
You are free to be creative with the design. If you have ideas that are not listed in the description, feel free to design them.
Thanks!!!
Family Insurance

```html
<!DOCTYPE html>
<html lang="en">
<head>
<meta charset="utf-8">
<title>DELVOR Flyer</title>
<link href="https://fonts.googleapis.com/css2?family=Montserrat:ital,wght@0,400;0,600;0,700;1,400&display=swap" rel="stylesheet">
<style>
  :root {
    --backdrop: #cdcdcd;
    --paper: #f9f9f9;
    --brand-red: #e5262f;
    --bar-grey: #8c8c8c;
    --rule-grey: #9a9a9a;
    --heading-grey: #5b5b5b;
    --body-grey: #8a8a8a;
    --white: #ffffff;
  }
  * { box-sizing: border-box; margin: 0; padding: 0; }
  html, body { width: 1200px; height: 800px; overflow: hidden; }
  body {
    background: var(--backdrop);
    font-family: "Montserrat", Arial, sans-serif;
    position: relative;
  }
  .flyer {
    position: absolute;
    left: 340px; top: 32px;
    width: 520px; height: 736px;
    background: var(--paper);
    overflow: hidden;
  }
  .top-bar {
    position: absolute; left: 0; top: 34px;
    width: 88px; height: 25px;
    background: var(--bar-grey);
  }
  .brand {
    position: absolute; left: 96px; top: 30px;
    display: flex; align-items: center; gap: 8px;
  }
  .brand-dot {
    width: 18px; height: 18px; border-radius: 50%;
    background: var(--brand-red);
  }
  .brand-name {
    color: var(--brand-red);
    font-weight: 700; font-size: 27px; letter-spacing: -0.5px;
    line-height: 1;
  }
  .top-rule {
    position: absolute; left: 305px; top: 57px;
    width: 155px; height: 1px; background: var(--rule-grey);
  }
  .hero {
    position: absolute; left: 37px; top: 115px;
    width: 406px; height: 406px;
  }
  .hero svg { display: block; }
  .hero-title {
    position: absolute; left: 80px; top: 303px;
    color: var(--brand-red);
    font-weight: 700; font-size: 31px; line-height: 40px;
    letter-spacing: -0.3px;
  }
  .hero-tagline {
    position: absolute; left: 80px; top: 397px;
    display: flex; align-items: center; gap: 6px;
    color: var(--white); font-size: 13px; font-weight: 400;
  }
  .hero-tagline::before {
    content: ""; width: 9px; height: 9px; background: var(--white);
  }
  .accent-bar {
    position: absolute; background: var(--bar-grey);
  }
  .accent-bar--long { left: 285px; top: 454px; width: 150px; height: 22px; }
  .accent-bar--short { left: 302px; top: 481px; width: 88px; height: 19px; }
  .info-block { position: absolute; }
  .info-block--about { left: 65px; top: 560px; width: 175px; }
  .info-block--contact { left: 277px; top: 574px; width: 175px; }
  .info-heading {
    display: flex; align-items: flex-end; gap: 6px;
    color: var(--heading-grey); font-weight: 600; font-size: 12.5px;
    margin-bottom: 12px;
  }
  .info-heading::after {
    content: ""; flex: 1; height: 1px; background: var(--rule-grey);
    margin-bottom: 3px;
  }
  .info-text {
    color: var(--body-grey); font-size: 8.5px; line-height: 12px;
    margin-bottom: 12px;
  }
  .info-label { color: var(--body-grey); font-size: 8.5px; line-height: 12px; }
  .info-value {
    color: var(--body-grey); font-size: 8.5px; line-height: 12px;
    font-style: italic; margin-bottom: 10px;
  }
  .web-link {
    display: flex; align-items: center; gap: 5px;
    color: var(--body-grey); font-size: 8.5px;
  }
  .web-link::before {
    content: ""; width: 5px; height: 5px; background: var(--heading-grey);
  }
</style>
</head>
<body>
  <main class="flyer">
    <div class="top-bar"></div>
    <div class="brand">
      <span class="brand-dot"></span>
      <span class="brand-name">Cedar Vale</span>
    </div>
    <div class="top-rule"></div>

    <div class="hero">
      <svg width="406" height="406" viewBox="0 0 406 406">
        <defs>
          <clipPath id="hero-clip"><circle cx="203" cy="203" r="203"/></clipPath>
          <linearGradient id="hero-tone" x1="0" y1="0" x2="0" y2="1">
            <stop offset="0" stop-color="#7f8a72"/>
            <stop offset="0.35" stop-color="#9aa09a"/>
            <stop offset="0.6" stop-color="#a9b0bd"/>
            <stop offset="1" stop-color="#c3c9d3"/>
          </linearGradient>
        </defs>
        <g clip-path="url(#hero-clip)">
          <rect width="406" height="406" fill="url(#hero-tone)" role="img" aria-label="Portrait photo of a smiling insurance agent in a light grey suit and navy tie, arms crossed, outdoors"/>
          <line x1="0" y1="183" x2="406" y2="132" stroke="#ffffff" stroke-width="1.5" opacity="0.8"/>
          <line x1="385" y1="100" x2="250" y2="406" stroke="#ffffff" stroke-width="1.5" opacity="0.9"/>
        </g>
      </svg>
    </div>

    <h1 class="hero-title">INSURANCE<br>PROFESSIONAL</h1>
    <p class="hero-tagline">ANY TEXT HERE</p>

    <div class="accent-bar accent-bar--long"></div>
    <div class="accent-bar accent-bar--short"></div>

    <section class="info-block info-block--about">
      <h2 class="info-heading">ABOUT US</h2>
      <p class="info-text">This is Quillmark's version of Lorem Ipsum. Proin gravida nibh vel velit auctor aliquet.</p>
      <p class="info-text">Aenean sollicitudin, lorem quis bibendum auctor, nisi elit consequat ipsum, nec sagittis sem nibh id elit.</p>
      <p class="web-link">www.delvorcover.com</p>
    </section>

    <section class="info-block info-block--contact">
      <h2 class="info-heading">CONTACT US</h2>
      <p class="info-label">Address:</p>
      <p class="info-value">No 24, Alder Row, Brookfield</p>
      <p class="info-label">Phone:</p>
      <p class="info-value">(55) 321 480 762</p>
      <p class="info-label">Email:</p>
      <p class="info-value">info@delvorcover.com</p>
    </section>
  </main>
</body>
</html>
```